New Restaurant Flyer more work need later!!

I am opening A new Restaurant The Copper Lantern
The theme of the restaurant is shabby chic
I have purchased 1950 furniture and the decor will be painted ( Mabel Farrow style Google Mabel Farrow.) The colours will be Tessa Greens.
I have no photos yet as the project has not started yet.
It is a pub style restaurant and the main feature is the Bar which has been built with an old altar which has been taken from a church.
The food will be all day
Breakfasts
Lunches
which will vary from sandwiches to light bites
Our Unique selling point are:
We Intend to do a grazing menu ( small plates )
The customer will maybe choose 3 as meal They will be served on wooden drift wood boards
for example
Sticky ribs Fish cakes And duck spring rolls.
Our main USP will be Steaks Fish And Chicken which will be cooked on a Wendel oven ( Google it)
Its a oven which uses real charcoal and cooked the same as you would in the summer in you garden./
We will also be selling cakes and coffee's
We will be selling traditional cask ales and fine wines.
this link is the details of the premises

http://www.brackwellagents.example/property/512?showstc=on&town=&multi_types=Restaurant+%2F+Cafe&unit_minarea=&unit_maxarea=&unit_areatype=&page=1
any questions email me
rowlinsk@mailbox.example
I will also be looking for additional marketing art work latter

Restaurant

```html
<!DOCTYPE html>
<html lang="en">
<head>
<meta charset="utf-8">
<title>The Copper Lantern – Now Open</title>
<link rel="stylesheet" href="https://fonts.googleapis.com/css2?family=Aldrich&family=Bebas+Neue&display=swap">
<style>
  :root {
    --sky: #c3e3f0;
    --sky-deep: #aed6e6;
    --slate: #5f8ba2;
    --slate-dark: #557f96;
    --white: #ffffff;
    --wood-light: #dfae70;
    --wood-mid: #d19a5a;
    --wood-dark: #c0884a;
  }
  * { margin: 0; padding: 0; box-sizing: border-box; }
  html, body { width: 800px; height: 1200px; overflow: hidden; }
  body { background: var(--sky); }

  .flyer {
    position: relative;
    width: 800px;
    height: 1200px;
    overflow: hidden;
    background: radial-gradient(ellipse at 50% 40%, var(--sky) 0%, var(--sky-deep) 100%);
    text-align: center;
  }

  .venue-name {
    position: absolute;
    top: 40px;
    left: 0;
    width: 100%;
    font-family: "Aldrich", sans-serif;
    font-weight: 400;
    color: var(--slate);
    text-transform: uppercase;
    line-height: 0.98;
    text-shadow: 1px 2px 3px rgba(40, 70, 90, 0.25);
  }
  .venue-name span { display: block; }
  .venue-name .line-short { font-size: 112px; letter-spacing: 4px; }
  .venue-name .line-mid { font-size: 112px; letter-spacing: 4px; }
  .venue-name .line-long { font-size: 104px; letter-spacing: 2px; }

  .announcement {
    position: absolute;
    top: 462px;
    left: 0;
    width: 100%;
    font-family: "Bebas Neue", sans-serif;
    font-size: 252px;
    line-height: 0.84;
    color: var(--white);
    letter-spacing: 2px;
    text-shadow: 2px 4px 6px rgba(40, 70, 90, 0.22);
  }
  .announcement span { display: block; }

  .menu-headline {
    position: absolute;
    top: 872px;
    left: 0;
    width: 100%;
    font-family: "Bebas Neue", sans-serif;
    font-size: 57px;
    color: var(--slate);
    letter-spacing: 1px;
    line-height: 1;
  }
  .menu-details {
    position: absolute;
    top: 936px;
    left: 0;
    width: 100%;
    font-family: "Bebas Neue", sans-serif;
    font-size: 27px;
    color: var(--slate-dark);
    letter-spacing: 0.5px;
    line-height: 1;
  }

  .counter-top {
    position: absolute;
    left: 0;
    bottom: 0;
    width: 800px;
    height: 191px;
    background: linear-gradient(180deg, var(--wood-light) 0%, var(--wood-mid) 55%, var(--wood-dark) 100%);
    box-shadow: 0 -3px 8px rgba(60, 80, 90, 0.2);
  }

  .location {
    position: absolute;
    top: 1061px;
    left: 0;
    width: 100%;
    font-family: "Bebas Neue", sans-serif;
    font-size: 58px;
    color: var(--white);
    letter-spacing: 1.5px;
    line-height: 1;
    text-shadow: 1px 2px 3px rgba(90, 55, 20, 0.3);
  }
  .contact-links {
    position: absolute;
    top: 1129px;
    left: 0;
    width: 100%;
    font-family: "Bebas Neue", sans-serif;
    font-size: 29px;
    color: var(--white);
    letter-spacing: 1px;
    line-height: 1;
    text-shadow: 1px 2px 3px rgba(90, 55, 20, 0.3);
  }
  .contact-links .divider { margin: 0 10px; }
</style>
</head>
<body>
  <main class="flyer">
    <h1 class="venue-name">
      <span class="line-short">The</span>
      <span class="line-mid">Copper</span>
      <span class="line-long">Lantern</span>
    </h1>

    <p class="announcement"><span>Now</span><span>Open</span></p>

    <p class="menu-headline">Breakfasts • Lunches • Grazing Menu</p>
    <p class="menu-details">Steaks Fish • Chicken • Cakes • Coffee • Traditional Cask Ales • Fine Wines</p>

    <div class="counter-top" role="img" aria-label="Light oak wooden floorboard texture"></div>

    <p class="location">Harrow Arcade, Eastmere, EM4</p>
    <p class="contact-links">Email<span class="divider">|</span>Contact Number<span class="divider">|</span>Website</p>
  </main>
</body>
</html>
```